Pixvane Set Up Ads for KELBY Property Management Company

We need a set of 6 ads of the following sizes created for Pixvane:

Medium rectangle: 300×250
Leaderboard: 728×90
Wide skyscraper: 160×600
Large rectangle: 300x600
Mobile leaderboard: 320×50
Billboard: 970x250

Here are the Formatting Guidelines (WEB ADS): https://help.pixvane-example.com/hc/en-us/articles/583920174-Ad-Content-and-Format-Guidelines

No animation - photos to link back to the website.

Here is the website: https://www.kelbyrenews-example.com/

Please try to copy the look and feel.

Here are some words for the ad - feel free to use creative liberties if you have something better or need less words.

1. KELBY. Results - Not Recommendations.
2. KELBY. Transform Your Business By Transforming Your Core.
3. It's time for better results. It's time to change your management company. KELBY.
4. What company couldn't benefit from a "fresh set of eyes?" Talk to Kelby.
5. Talk to KELBY about what they can do for your bottom-line.

Target Market(s)

People who have already visited our website. These people will be private owners, REITs, or Private Equity people looking for a new management company for their underperforming asset.

Industry/Entity Type

Property Management

Font styles to use
Sans Serif

Colors
f37122
6b449b
33b8a4

Requirements
Must have
• logo - at least the "O" unless you can find other ways to pull it back to the website.
Nice to have
• Photos from kelbyrenews-example.com to remind the user what website we are when they are redirected - I purchased from lumbra photos off tilde grove.
Should not have
• Animation

```html
<!DOCTYPE html>
<html lang="en">
<head>
<meta charset="utf-8">
<title>KELBY Billboard Ad</title>
<link rel="stylesheet" href="https://fonts.googleapis.com/css2?family=PT+Sans:wght@400;700&display=swap">
<style>
  :root {
    --brand-purple: #6b449b;
    --brand-purple-deep: #4a2a73;
    --ink: #141414;
    --paper: #ffffff;
    --wood-light: #e9dccb;
    --wood-mid: #d9c3a6;
    --tint-blue: #bcdde6;
    --tint-red: #f2b7a6;
    --tint-yellow: #f3ebb0;
    --tint-green: #cfe5b8;
  }
  * { box-sizing: border-box; margin: 0; padding: 0; }
  html, body {
    width: 1200px;
    height: 309px;
    overflow: hidden;
    background: var(--paper);
  }
  .ad {
    position: relative;
    width: 1200px;
    height: 309px;
    overflow: hidden;
    font-family: "PT Sans", sans-serif;
    color: var(--ink);
  }
  .ad__photo {
    position: absolute;
    inset: 0;
    background:
      radial-gradient(circle at 22% 30%, var(--tint-blue) 0, transparent 22%),
      radial-gradient(circle at 16% 85%, var(--tint-red) 0, transparent 24%),
      radial-gradient(circle at 40% 35%, var(--tint-yellow) 0, transparent 14%),
      radial-gradient(circle at 58% 55%, var(--tint-green) 0, transparent 20%),
      radial-gradient(circle at 90% 70%, var(--wood-mid) 0, transparent 28%),
      linear-gradient(120deg, var(--wood-light), var(--wood-mid));
  }
  .ad__wash {
    position: absolute;
    top: 0;
    bottom: 0;
    left: 309px;
    right: 20px;
    background: rgba(255, 255, 255, 0.72);
  }
  .ad__divider {
    position: absolute;
    top: 0;
    bottom: 0;
    left: 306px;
    width: 6px;
    background: var(--brand-purple);
  }
  .brand {
    position: absolute;
    left: 22px;
    top: 38px;
    width: 220px;
    height: 220px;
    display: flex;
    align-items: center;
    justify-content: center;
    gap: 10px;
  }
  .brand__dot {
    width: 26px;
    height: 26px;
    border-radius: 50%;
    background: var(--brand-purple);
  }
  .brand__name {
    font-weight: 700;
    font-size: 46px;
    color: var(--brand-purple);
    letter-spacing: 1px;
  }
  .message {
    position: absolute;
    left: 328px;
    top: 108px;
  }
  .message__headline {
    font-weight: 700;
    font-size: 31px;
    line-height: 1.2;
    letter-spacing: 0.3px;
  }
  .message__sub {
    font-weight: 400;
    font-size: 28.5px;
    line-height: 1.3;
    letter-spacing: 0.3px;
  }
  .cta {
    position: absolute;
    left: 662px;
    top: 231px;
    width: 186px;
    height: 54px;
    display: flex;
    align-items: center;
    justify-content: center;
    border: 3px solid var(--brand-purple);
    background: var(--paper);
    color: var(--ink);
    font-weight: 700;
    font-size: 21px;
    text-decoration: none;
    letter-spacing: 0.3px;
  }
</style>
</head>
<body>
  <div class="ad">
    <div class="ad__photo" role="img" aria-label="Photo of colourful wooden tangram pieces on a wooden table, softly faded"></div>
    <div class="ad__wash"></div>
    <div class="ad__divider"></div>

    <div class="brand">
      <span class="brand__dot"></span>
      <span class="brand__name">KELBY</span>
    </div>

    <div class="message">
      <p class="message__headline">IT'S TIME FOR BETTER RESULTS.</p>
      <p class="message__sub">IT'S TIME TO CHANGE YOUR MANAGEMENT COMPANY.</p>
    </div>

    <a class="cta" href="https://www.kelbyrenews-example.com/">TALK TO KELBY</a>
  </div>
</body>
</html>
```